need eczema bath soak label/bag

need you to recreate this please. ai file. recreate this exact image please. ...if you want a big tip, create some different styles.

Colors
0054AA
0677BA
7BADD7
CADEEF
E8F1F8

```html
<!DOCTYPE html>
<html lang="en">
<head>
<meta charset="utf-8">
<title>The Ocean Healed Soak – Bath Soak Label</title>
<link rel="stylesheet" href="https://fonts.googleapis.com/css2?family=Outfit:wght@300;400;600;700;800&display=swap">
<style>
  :root {
    --ink: #0c1f33;
    --white: #ffffff;
    --mist: #e8f1f8;
    --foam: #cadeef;
    --surf-light: #7badd7;
    --surf: #0677ba;
    --deep: #0054aa;
    --wet-sand: #cfc3ad;
    --sand: #dcb57c;
    --sand-dark: #d0a265;
  }
  * { margin: 0; padding: 0; box-sizing: border-box; }
  html, body { width: 720px; height: 1200px; overflow: hidden; background: var(--white); }
  .label {
    position: relative;
    width: 720px;
    height: 1200px;
    overflow: hidden;
    font-family: "Outfit", sans-serif;
    color: var(--ink);
  }
  .shoreline {
    position: absolute;
    inset: 0;
    background: linear-gradient(to bottom,
      var(--white) 0px,
      var(--white) 262px,
      var(--mist) 285px,
      var(--surf-light) 320px,
      #2f8fc0 370px,
      var(--surf) 440px,
      #3897c2 520px,
      var(--surf-light) 580px,
      var(--foam) 630px,
      var(--white) 665px,
      var(--wet-sand) 720px,
      #d8cbb4 800px,
      #e2d3b8 850px,
      var(--sand) 880px,
      var(--sand-dark) 1050px,
      var(--sand) 1200px);
  }
  .product-title {
    position: absolute;
    left: 0;
    width: 720px;
    text-align: center;
    font-weight: 800;
    line-height: 1;
  }
  .title-the { top: 127px; font-size: 46px; letter-spacing: 0.5px; }
  .title-line { font-size: 106px; letter-spacing: -1px; }
  .title-ocean { top: 192px; }
  .title-healed { top: 306px; }
  .title-soak { top: 418px; }
  .claim {
    position: absolute;
    top: 538px;
    left: 0;
    width: 720px;
    text-align: center;
    font-size: 23px;
    font-weight: 300;
    line-height: 31px;
  }
  .treatment {
    position: absolute;
    top: 652px;
    left: 0;
    width: 720px;
    text-align: center;
    font-size: 27px;
    font-weight: 700;
  }
  .net-weight {
    position: absolute;
    top: 680px;
    left: 0;
    width: 720px;
    height: 70px;
  }
  .net-weight text {
    font-family: "Outfit", sans-serif;
    font-size: 35px;
    font-weight: 600;
    fill: var(--ink);
  }
  .format {
    position: absolute;
    top: 756px;
    left: 0;
    width: 720px;
    text-align: center;
    font-size: 25px;
    font-weight: 300;
  }
  .brand {
    position: absolute;
    top: 1010px;
    left: 0;
    width: 720px;
    display: flex;
    justify-content: center;
    align-items: center;
    gap: 12px;
  }
  .brand-mark {
    width: 16px;
    height: 16px;
    background: var(--ink);
  }
  .brand-name {
    font-size: 20px;
    font-weight: 700;
    letter-spacing: 6px;
    color: var(--ink);
  }
</style>
</head>
<body>
  <main class="label">
    <div class="shoreline" role="img" aria-label="Aerial photograph of turquoise ocean waves breaking into white foam over a sandy beach"></div>

    <h1>
      <span class="product-title title-the">THE</span>
      <span class="product-title title-line title-ocean">OCEAN</span>
      <span class="product-title title-line title-healed">HEALED</span>
      <span class="product-title title-line title-soak">SOAK</span>
    </h1>

    <p class="claim">bath soak to relieve symptoms<br>of mid eczema &amp; itchy, irritated,<br>dry skin</p>

    <p class="treatment">SOOTHING TREATMENT</p>

    <svg class="net-weight" viewBox="0 0 720 70" aria-label="170g / 60oz">
      <defs>
        <path id="weight-arc" d="M262,30 Q361,70 460,30" fill="none"/>
      </defs>
      <text><textPath href="#weight-arc" startOffset="50%" text-anchor="middle">170g/60oz</textPath></text>
    </svg>

    <p class="format">BATH SOAK</p>

    <div class="brand">
      <span class="brand-mark"></span>
      <span class="brand-name">TIDEWELL</span>
    </div>
  </main>
</body>
</html>
```